two-fold brochure design for oral product

Folded dimension: 21cm*9.5 cm, unfolded dimension: 21*19 cm.
CMYK, 300 pixels, ready for printing.
I hope the brochure would be upmarket.
If you need more elements about our products or brand for this design, pls let me know.

Target Market(s)

female from 20-40

```html
<!DOCTYPE html>
<html lang="en">
<head>
<meta charset="utf-8">
<title>Aligner Gel – Brochure</title>
<link href="https://fonts.googleapis.com/css2?family=Montserrat:ital,wght@0,700;0,800;1,700&family=Raleway:wght@400;500&display=swap" rel="stylesheet">
<style>
  :root{
    --leaf:#3e5a26;
    --leaf-deep:#33491f;
    --paper:#ffffff;
    --backdrop:#eeeeee;
    --ink:#222222;
    --ink-soft:#333333;
    --bottle-top:#6e6a2a;
    --bottle-low:#4a4a1c;
  }
  *{margin:0;padding:0;box-sizing:border-box}
  html,body{width:753px;height:1200px;overflow:hidden;background:var(--backdrop)}
  .stage{position:absolute;left:0;top:0;width:960px;height:1530px;transform:scale(0.7844);transform-origin:0 0}
  .panel{position:absolute;left:104px;width:752px;height:680px;overflow:hidden}
  .panel--outside{top:48px;background:var(--leaf);color:var(--paper)}
  .panel--inside{top:785px;background:var(--paper);color:var(--ink)}
  .abs{position:absolute}
  .shape{position:absolute;left:0;top:0;width:752px;height:680px}
  .heading{font-family:"Montserrat",sans-serif;font-weight:800;letter-spacing:.3px}
  .subhead{font-family:"Montserrat",sans-serif;font-weight:700;font-style:italic;font-size:16.5px;margin-bottom:18px}
  .copy{font-family:"Raleway",sans-serif;font-weight:400;font-size:15px;line-height:18.2px}
  .copy p{margin-bottom:18px}
  .usage{left:40px;top:58px;width:310px}
  .usage .heading{font-size:31px;margin-bottom:52px}
  .usage .block{margin-bottom:4px}
  .brand{right:48px;top:60px;font-family:"Montserrat",sans-serif;font-weight:800;font-size:66px;line-height:64px;color:var(--paper);text-align:right}
  .bottle{background:linear-gradient(180deg,#e8e8e8 0 24%,var(--bottle-top) 24% 55%,var(--bottle-low) 100%);border-radius:14px 14px 8px 8px}
  .bottle--cover{left:405px;top:284px;width:110px;height:274px}
  .bottle--inside{left:502px;top:364px;width:112px;height:280px}
  .product-name{right:38px;top:448px;font-family:"Montserrat",sans-serif;font-weight:700;font-size:47px;line-height:46px;color:var(--leaf);text-align:right}
  .claims{right:38px;top:562px;text-align:right;color:var(--ink);font-size:14.5px;line-height:17px}
  .origin{right:38px;top:630px;color:var(--ink);font-size:14.5px}
  .reasons-title{left:42px;top:102px;font-size:33px;line-height:42px;color:var(--paper)}
  .reasons{left:41px;top:276px;width:300px}
  .reasons .item{height:130px}
  .ingredients{left:439px;top:46px;width:240px;color:var(--paper)}
  .ingredients .heading{font-size:31px;margin-bottom:26px}
  .ingredients .caps{text-transform:uppercase}
</style>
</head>
<body>
<div class="stage">

  <section class="panel panel--outside">
    <svg class="shape" viewBox="0 0 752 680" aria-hidden="true">
      <path d="M341,680 C470,600 540,470 585,370 C605,320 618,292 630,272 C612,350 650,430 752,450 L752,680 Z" fill="#ffffff"/>
      <path d="M690,282 C662,360 690,428 752,446 L752,438 C706,418 684,360 690,282 Z" fill="#ffffff"/>
    </svg>

    <div class="abs usage">
      <h2 class="heading">HOW TO USE:</h2>
      <div class="block">
        <h3 class="subhead">— Daily oral care</h3>
        <div class="copy">
          <p>Brush your teeth with drops on top of toothpaste</p>
          <p>Squeeze the toothpaste onto the tooth-brush first, then put a drop of essence on the toothpaste and brush your teeth thoroughly for at least three minutes</p>
        </div>
      </div>
      <div class="block">
        <h3 class="subhead">— Topical oral care</h3>
        <div class="copy">
          <p>Drop and penetrate between the teeth</p>
          <p>Drop the essence between your teeth or on the uncomfortable area, do not rinse your mouth after dripping, and do not drink water for half an hour.</p>
        </div>
      </div>
      <div class="block">
        <h3 class="subhead">— Special oral care</h3>
        <div class="copy">
          <p>Drop in braces and wear</p>
          <p>Remove the invisible braces or clear retainers, and drip gum essence into the braces to wear.</p>
        </div>
      </div>
    </div>

    <div class="abs brand">lumi<br>drop</div>

    <div class="abs bottle bottle--cover" role="img" aria-label="Product photo: dropper bottle of Aligner Gel"></div>

    <div class="abs product-name">Aligner<br>Gel</div>
    <div class="abs copy claims">Natural herbal extracts<br>Contain a variety of actives<br>Improve the condition of oral cavity</div>
    <div class="abs copy origin">origin Manufactured in Taiwan</div>
  </section>

  <section class="panel panel--inside">
    <svg class="shape" viewBox="0 0 752 680" aria-hidden="true">
      <path d="M0,36 H268 A108.5,108.5 0 0 1 268,253 H0 Z" fill="#3e5a26"/>
      <path d="M414,0 H703 V505 A144.5,144.5 0 0 1 414,505 Z" fill="#3e5a26"/>
    </svg>

    <h2 class="abs heading reasons-title">REASONS<br>TO CHOOSE:</h2>

    <div class="abs reasons">
      <div class="item">
        <h3 class="subhead">— Freshen breath</h3>
        <p class="copy">Effectively inhibit the growth of harmful bacteria in the mouth, improve oral health, and get rid of odor.</p>
      </div>
      <div class="item">
        <h3 class="subhead">— Nourish and repair</h3>
        <p class="copy">Improve immunity, so that the damaged oral epidermis and gum tissue can be repaired in time.</p>
      </div>
      <div class="item">
        <h3 class="subhead">— Soothe discomfort</h3>
        <p class="copy">Harnesses the natural properties of herbs to reduce the sensitivity of the pain nerves in the mouth.</p>
      </div>
    </div>

    <div class="abs ingredients">
      <h2 class="heading">INGREDIENTS:</h2>
      <div class="copy">
        <p>Acerola extract, Aloe Vera extract, Chamomile extract, Sage extract, Honeysuckle extract, Angelica extract, Coptis extract, Rehmannia Root extract, Echinacea Purpurea extract.</p>
        <p class="caps" style="margin-top:26px">Protect and nourish</p>
        <p>Keep Your Teeth and Gums in Better Conditions.</p>
      </div>
    </div>

    <div class="abs bottle bottle--inside" role="img" aria-label="Product photo: dropper bottle of Aligner Gel"></div>
  </section>

</div>
</body>
</html>
```